Professional Word template for reports and concepts

I need a Word template for reports, concepts, guidelines, and lead magnets:
- Cover page
- Table of contents
- Text with various formatting templates for notes, reminders, quotes, visualizations
- Headers and footers
- etc.
The uploaded documents contain a detailed briefing document with all requirements.
Our website is www.velbrantik.de
Industry/Entity Type
Profesional Services
Font styles to use
Other font styles liked:
- Open Sans
Look and feel
Each slider illustrates characteristics of the customer's brand and the style your logo design should communicate.

```html
<!DOCTYPE html>
<html lang="de">
<head>
<meta charset="utf-8">
<title>Berichtsvorlage – Seitenübersicht</title>
<link rel="stylesheet" href="https://fonts.googleapis.com/css2?family=Open+Sans:wght@400;600;700;800&display=swap">
<style>
:root{
  --navy:#1e3765;
  --navy-soft:#2c4a80;
  --orange:#e8892a;
  --sky:#cfdff0;
  --sky-soft:#eaf1f8;
  --text:#444b55;
  --rule:#d5d9df;
  --stage:#e6e7ea;
  --paper:#ffffff;
}
*{box-sizing:border-box;margin:0;padding:0}
html,body{width:891px;height:1200px;overflow:hidden}
body{background:var(--stage);font-family:"Open Sans",Arial,sans-serif;color:var(--text);position:relative}
.page{position:absolute;width:272px;height:384px;background:var(--paper);box-shadow:0 1px 3px rgba(0,0,0,.18);overflow:hidden}
.col1{left:10px}.col2{left:310px}.col3{left:609px}
.row1{top:6px}.row2{top:408px}.row3{top:810px}
.brand{position:absolute;top:10px;right:14px;display:flex;align-items:center;gap:3px;font-weight:700;font-size:7px;color:var(--navy);z-index:2}
.brand i{width:6px;height:6px;border-radius:50%;background:var(--orange);display:block}
.page-footer{position:absolute;left:18px;right:18px;bottom:10px;border-top:.6px solid var(--rule);padding-top:3px;font-size:3.6px;display:flex;justify-content:space-between}
.body{position:absolute;left:20px;right:20px;top:30px}
h2{font-size:9px;color:var(--navy);font-weight:700;margin:0 0 6px}
h3{font-size:5px;color:var(--navy);font-weight:700;margin:6px 0 3px}
p,li{font-size:3.6px;line-height:5.2px;margin-bottom:3px}
ul{list-style:none}
li{padding-left:6px;position:relative;margin-bottom:1.5px}
li:before{content:"";position:absolute;left:0;top:1.8px;width:2px;height:2px;background:var(--orange)}
.kicker{color:var(--orange);font-weight:700;font-size:8px;letter-spacing:.3px}
.cover-title{color:var(--navy);font-weight:800;font-size:12px;line-height:14px;text-transform:uppercase}
.cover-visual{position:absolute;left:-40px;top:-40px;width:186px;height:186px;border-radius:50%;background:radial-gradient(circle at 60% 60%,#dbe7f4 0%,var(--sky) 70%)}
.meta{display:flex;gap:30px;font-size:3.8px;line-height:5.2px}
.meta b{color:var(--navy);display:block;font-size:4.2px}
.toc-row{display:flex;font-size:4px;line-height:7px}
.toc-row .dots{flex:1;border-bottom:.6px dotted #9aa3ae;margin:0 3px 2px}
.toc-row.sub{padding-left:8px;font-size:3.7px}
.toc-row.main{font-weight:700;color:var(--navy)}
.feature{display:flex;gap:8px;margin-bottom:12px}
.feature .icon{flex:none;width:22px;height:22px;border-radius:50%;background:var(--sky-soft);border:1px solid var(--sky);display:flex;align-items:center;justify-content:center}
.feature h3{margin-top:0}
.note{background:var(--sky-soft);border-left:2px solid var(--navy);padding:4px 6px;margin:5px 0}
.note.accent{border-left-color:var(--orange);background:#fdf2e6}
table{width:100%;border-collapse:collapse;font-size:3.6px;margin:4px 0}
td,th{border-bottom:.5px solid var(--rule);padding:2px 3px;text-align:left}
th{background:var(--navy);color:#fff;font-weight:600}
td.num{text-align:right}
.badge{background:var(--sky);border-radius:2px}
.seal{width:18px;height:18px;border-radius:50%;background:var(--navy-soft)}
</style>
</head>
<body>

<section class="page col1 row1">
  <div class="brand"><i></i>velbrantik</div>
  <div class="cover-visual" role="img" aria-label="Grafik der Phasen im Vertriebsprozess"></div>
  <div style="position:absolute;left:20px;top:182px;right:20px">
    <div class="kicker">PROJEKT:</div>
    <div class="cover-title">Einführung Norvo CRM,<br>inkl. Digitalisierung<br>des Sales-Prozesses</div>
  </div>
  <div class="meta" style="position:absolute;left:20px;top:290px">
    <div><b>Erstellt für</b>Muster GmbH<br>Abteilung Vertrieb</div>
    <div><b>Erstellt von</b>velbrantik<br>www.velbrantik.de</div>
  </div>
  <div style="position:absolute;left:0;right:0;bottom:0;height:5px;background:var(--orange)"></div>
</section>

<section class="page col2 row1">
  <div class="brand"><i></i>velbrantik</div>
  <div style="position:absolute;left:0;right:0;top:34px;height:210px;background:var(--navy)">
    <div style="position:absolute;left:20px;top:120px;right:20px">
      <div class="kicker">PROJEKT:</div>
      <div class="cover-title" style="color:#fff">Einführung Norvo CRM,<br>inkl. Digitalisierung<br>des Sales-Prozesses</div>
    </div>
  </div>
  <div class="meta" style="position:absolute;left:20px;top:290px">
    <div><b>Erstellt für</b>Muster GmbH<br>Abteilung Vertrieb</div>
    <div><b>Erstellt von</b>velbrantik<br>www.velbrantik.de</div>
  </div>
  <div style="position:absolute;left:0;right:0;bottom:0;height:5px;background:var(--orange)"></div>
</section>

<section class="page col3 row1">
  <div class="brand"><i></i>velbrantik</div>
  <div class="body">
    <h2>Inhaltsverzeichnis</h2>
    <div class="toc-row main">1. Ihr Partner als Kreativteam<span class="dots"></span>3</div>
    <div class="toc-row sub">1.1 Unser Ansatz<span class="dots"></span>3</div>
    <div class="toc-row sub">1.2 Leistungen im Überblick<span class="dots"></span>3</div>
    <div class="toc-row main">2. Empfehlungen zur Umsetzung<span class="dots"></span>4</div>
    <div class="toc-row sub">2.1 Ausgangslage<span class="dots"></span>4</div>
    <div class="toc-row sub">2.2 Zielbild des Prozesses<span class="dots"></span>4</div>
    <div class="toc-row sub">2.3 Technische Einrichtung<span class="dots"></span>5</div>
    <div class="toc-row sub">2.4 Schulung und Einführung<span class="dots"></span>5</div>
    <div class="toc-row main">3. Ihre Investition<span class="dots"></span>6</div>
    <div class="toc-row sub">3.1 Leistungspakete<span class="dots"></span>6</div>
    <div class="toc-row main">4. Ihr Partner im Detail<span class="dots"></span>6</div>
    <div class="toc-row sub">4.1 Zertifikate<span class="dots"></span>7</div>
    <div class="toc-row sub">4.2 Referenzen<span class="dots"></span>7</div>
    <div class="toc-row main">5. Anhang<span class="dots"></span>8</div>
  </div>
  <div class="page-footer"><span>www.velbrantik.de</span><span>2</span></div>
</section>

<section class="page col1 row2">
  <div class="brand"><i></i>velbrantik</div>
  <div class="body">
    <h2>1. Ihr Partner als Kreativteam</h2>
    <div class="feature">
      <div class="icon"><svg width="10" height="10" viewBox="0 0 10 10"><circle cx="5" cy="5" r="4" fill="none" stroke="var(--navy)" stroke-width="1"/><path d="M3 5l1.5 1.5L7 3.5" fill="none" stroke="var(--orange)" stroke-width="1"/></svg></div>
      <div><h3>Erfahrung aus vielen Projekten</h3><p>Wir begleiten Unternehmen seit Jahren bei der Einführung digitaler Vertriebsprozesse. Unsere Berater kennen typische Hürden und sorgen für einen ruhigen Projektverlauf ohne Umwege.</p></div>
    </div>
    <div class="feature">
      <div class="icon"><svg width="10" height="10" viewBox="0 0 10 10"><rect x="1.5" y="1.5" width="7" height="7" fill="none" stroke="var(--navy)" stroke-width="1"/><path d="M3 5h4M5 3v4" stroke="var(--orange)" stroke-width="1"/></svg></div>
      <div><h3>Lösungen aus einer Hand</h3><p>Von der Analyse über die Konfiguration bis zur Schulung erhalten Sie alle Leistungen aus einer Hand. Ein fester Ansprechpartner koordiniert alle Schritte und hält Sie stets informiert.</p></div>
    </div>
    <div class="feature">
      <div class="icon"><svg width="10" height="10" viewBox="0 0 10 10"><path d="M1 8l3-3 2 2 3-4" fill="none" stroke="var(--navy)" stroke-width="1"/><circle cx="9" cy="3" r="1" fill="var(--orange)"/></svg></div>
      <div><h3>Messbare Ergebnisse</h3><p>Klare Kennzahlen zeigen früh, wie sich Ihr Vertrieb entwickelt. Wir definieren gemeinsam Ziele und prüfen regelmäßig, ob die Maßnahmen wirken und wo nachgesteuert werden sollte.</p></div>
    </div>
    <div class="note"><p style="margin:0">Hinweis: Alle Leistungen lassen sich flexibel an Ihre internen Abläufe und Ressourcen anpassen.</p></div>
  </div>
  <div class="page-footer"><span>www.velbrantik.de</span><span>3</span></div>
</section>

<section class="page col2 row2">
  <div class="brand"><i></i>velbrantik</div>
  <div class="body">
    <h2>2. Empfehlungen zur Umsetzung</h2>
    <div class="note"><h3 style="margin-top:0">Ziel dieses Kapitels</h3><p style="margin:0">Hier fassen wir zusammen, welche Schritte wir für eine erfolgreiche Einführung empfehlen.</p></div>
    <h3>Ausgangslage</h3>
    <p>Derzeit werden Kontakte und Angebote in mehreren Listen gepflegt. Informationen gehen verloren, Nachfassaktionen erfolgen unregelmäßig und Auswertungen kosten viel Zeit.</p>
    <h3>Zielbild des Prozesses</h3>
    <ul><li>Zentrale Datenbasis für alle Kundenkontakte</li><li>Automatische Erinnerungen für offene Angebote</li><li>Transparente Pipeline für die Geschäftsleitung</li><li>Einheitliche Vorlagen für Angebote und E-Mails</li></ul>
    <h3>Technische Einrichtung</h3>
    <p>Wir richten das System ein, übernehmen bestehende Daten und binden vorhandene Werkzeuge wie Kalender und E-Mail an. Anschließend testen wir alle Abläufe mit Ihrem Team.</p>
    <div class="note accent"><p style="margin:0">„Ein guter Prozess macht den Vertrieb planbar und entlastet das ganze Team.“</p></div>
    <p>Die Einführung erfolgt schrittweise, damit der laufende Betrieb jederzeit gesichert bleibt.</p>
  </div>
  <div class="page-footer"><span>www.velbrantik.de</span><span>4</span></div>
</section>

<section class="page col3 row2">
  <div class="brand"><i></i>velbrantik</div>
  <div class="body">
    <h3 style="margin-top:0">Schulung und Einführung</h3>
    <ul><li>Workshop zur Abstimmung der Anforderungen</li><li>Konfiguration von Feldern, Phasen und Rollen</li><li>Import und Bereinigung der Bestandsdaten</li><li>Schulung der Anwender in kleinen Gruppen</li><li>Begleitung in den ersten Wochen nach Start</li></ul>
    <p>Alle Schulungen finden wahlweise vor Ort oder online statt. Die Teilnehmer erhalten kompakte Unterlagen zum Nachschlagen.</p>
    <h3>Berichte und Auswertungen</h3>
    <ul><li>Übersicht über offene Verkaufschancen</li><li>Umsatzprognose pro Quartal</li><li>Aktivitäten je Mitarbeiter</li></ul>
    <p>Die Berichte werden an Ihre Kennzahlen angepasst und stehen jederzeit tagesaktuell zur Verfügung.</p>
    <h3>Datenschutz</h3>
    <p>Die Speicherung erfolgt in Rechenzentren innerhalb der EU. Zugriffsrechte werden nach Rollen vergeben und dokumentiert.</p>
    <h3>Nächste Schritte</h3>
    <ul><li>Abstimmung des Zeitplans</li><li>Benennung der Projektverantwortlichen</li><li>Start mit dem Auftaktworkshop</li></ul>
  </div>
  <div class="page-footer"><span>www.velbrantik.de</span><span>5</span></div>
</section>

<section class="page col1 row3">
  <div class="brand"><i></i>velbrantik</div>
  <div class="body">
    <h2>3. Ihre Investition</h2>
    <p>Die folgenden Pakete bilden den empfohlenen Projektumfang ab. Alle Preise verstehen sich zuzüglich Mehrwertsteuer.</p>
    <table>
      <tr><th>Leistung</th><th style="text-align:right">Betrag</th></tr>
      <tr><td>Analyse und Konzept</td><td class="num">2.400 €</td></tr>
      <tr><td>Einrichtung und Datenimport</td><td class="num">4.800 €</td></tr>
      <tr><td>Schulung der Anwender</td><td class="num">1.600 €</td></tr>
      <tr><td><b>Gesamt</b></td><td class="num"><b>8.800 €</b></td></tr>
    </table>
    <h2 style="margin-top:12px">4. Ihr Partner im Detail</h2>
    <div style="display:flex;gap:8px">
      <div class="badge" style="flex:none;width:34px;height:44px;background:var(--navy-soft)" role="img" aria-label="Partnerabzeichen"></div>
      <p>Als zertifizierter Partner verfügen wir über geprüftes Fachwissen und direkten Zugang zum Hersteller. So profitieren Sie von schnellen Antworten und bewährten Methoden.</p>
    </div>
  </div>
  <div class="page-footer"><span>www.velbrantik.de</span><span>6</span></div>
</section>

<section class="page col2 row3">
  <div class="brand"><i></i>velbrantik</div>
  <div class="body">
    <div style="display:flex;gap:6px;margin-bottom:8px">
      <div class="seal" style="flex:none" role="img" aria-label="Zertifikatssiegel"></div>
      <p style="flex:1">Zertifiziert für Beratung und Implementierung von CRM-Systemen im Mittelstand.</p>
    </div>
    <div style="display:flex;gap:6px;margin-bottom:8px">
      <div class="badge" style="flex:none;width:30px;height:14px;background:var(--orange)" role="img" aria-label="Auszeichnung"></div>
      <p style="flex:1">Ausgezeichnet für herausragende Kundenzufriedenheit im Jahr der Bewertung.</p>
    </div>
    <div style="display:flex;gap:6px;margin-bottom:8px">
      <div class="badge" style="flex:none;width:30px;height:14px" role="img" aria-label="Partnerlisting"></div>
      <p style="flex:1">Gelistet im offiziellen Partnerverzeichnis für die Region Deutschland.</p>
    </div>
    <h3>Leistung – Preisübersicht für das digitale Sales-Team</h3>
    <table>
      <tr><th>Paket</th><th>Umfang</th><th style="text-align:right">Preis</th></tr>
      <tr><td>Start</td><td>bis 5 Nutzer</td><td class="num">1.900 €</td></tr>
      <tr><td>Plus</td><td>bis 15 Nutzer</td><td class="num">3.900 €</td></tr>
      <tr><td>Pro</td><td>ab 16 Nutzer</td><td class="num">auf Anfrage</td></tr>
    </table>
  </div>
  <div class="page-footer"><span>www.velbrantik.de</span><span>7</span></div>
</section>

<section class="page col3 row3">
  <div class="brand"><i></i>velbrantik</div>
  <div class="body">
    <div class="seal" style="margin:0 0 8px auto;width:16px;height:16px" role="img" aria-label="Qualitätssiegel"></div>
    <h3 style="margin-top:0">Referenzen</h3>
    <p>Unsere Kunden stammen aus Handel, Industrie und Dienstleistung. Gerne nennen wir Ihnen Ansprechpartner, die über ihre Erfahrungen berichten.</p>
    <h3>Zusammenarbeit</h3>
    <p>Wir arbeiten partnerschaftlich, offen und mit klaren Absprachen. Jede Projektphase endet mit einer kurzen Abnahme, damit Sie jederzeit den Überblick behalten.</p>
    <h3>Kontakt</h3>
    <p>Für Rückfragen zu diesem Konzept stehen wir Ihnen gerne zur Verfügung. Wir freuen uns auf die gemeinsame Umsetzung.</p>
    <p>velbrantik · www.velbrantik.de</p>
  </div>
  <div class="page-footer"><span>www.velbrantik.de</span><span>8</span></div>
</section>

</body>
</html>
```